Residential Construction Company needs flyer designed.

We need a flyer design for a residential Rain Gutter and Screen room company. We have over 50 years in the remodeling industry and service all of Middle Georgia. We want the brochure to highlight our wonderful managerial staff to our great instillation crews. We also want to showcase the high-quality products that we use, gutter, leaf protection, screen rooms and sunrooms and the quality craftsmanship homeowners will receive when they choose to go with our company.

```html
<!DOCTYPE html>
<html lang="en">
<head>
<meta charset="utf-8">
<title>Hartwell Gutters &amp; Exteriors – Flyer</title>
<link href="https://fonts.googleapis.com/css2?family=Montserrat:wght@500;600;700&family=Questrial&display=swap" rel="stylesheet">
<style>
  :root{
    --navy:#052a4d;
    --teal:#05a99a;
    --teal-text:#12b3a0;
    --blue:#1a76c2;
    --light-blue:#6eb6ee;
    --card:#e4e4e6;
    --ink:#2b2f7a;
    --grey-text:#555;
    --white:#fff;
  }
  *{box-sizing:border-box;margin:0;padding:0}
  html,body{width:848px;height:1200px;overflow:hidden;background:#a19d9f}
  .flyer{position:relative;width:848px;height:1200px;background:var(--navy);font-family:"Questrial",sans-serif;color:var(--white)}
  .hero{position:absolute;left:0;top:0;width:848px;height:305px;background:linear-gradient(180deg,#8fc3e8 0%,#b9cfdc 30%,#9c9489 55%,#4d4f5a 80%,#2f3440 100%)}
  .brand{position:absolute;left:560px;top:40px;width:270px;text-align:center;font-family:"Montserrat",sans-serif;font-weight:700;font-size:22px;line-height:1.1;color:var(--blue)}
  .contact-phone{position:absolute;left:267px;top:306px;width:170px;height:41px;background:var(--teal);font-size:23px;display:flex;align-items:center;justify-content:center}
  .contact-email{position:absolute;left:444px;top:306px;width:404px;height:41px;background:var(--blue);font-size:20px;display:flex;align-items:center;justify-content:center}
  .photo{position:absolute;width:170px;border:6px solid var(--white)}
  .photo.framed-blue{border-color:var(--light-blue)}
  .p1{left:35px;top:338px;height:174px;background:linear-gradient(135deg,#9a9a98 0%,#7d7e7c 50%,#5f8a3c 75%,#6fa24a 100%)}
  .p2{left:222px;top:383px;height:175px;background:linear-gradient(180deg,#eef2f4 0%,#dfe6ea 40%,#8bb07a 60%,#c9c7c2 100%)}
  .p3{left:35px;top:529px;height:174px;background:linear-gradient(180deg,#c9d2dc 0%,#6e6660 25%,#25262a 50%,#2a2b2e 75%,#b8b5ae 100%)}
  .p4{left:222px;top:574px;height:175px;background:linear-gradient(180deg,#f1f1f0 0%,#9aa19c 35%,#e8e8e6 65%,#8f8a84 100%)}
  .headline{position:absolute;left:411px;top:362px;font-family:"Montserrat",sans-serif;font-weight:600;font-size:31px;line-height:45px;color:var(--teal-text);white-space:nowrap}
  .services-title{position:absolute;left:412px;top:461px;font-weight:400;font-size:28px;color:var(--teal-text)}
  .services-list{position:absolute;left:414px;top:500px;list-style:none;font-size:18px;color:var(--teal-text)}
  .services-list li{height:32.4px;display:flex;align-items:center}
  .services-list li::before{content:"";width:5px;height:5px;border-radius:50%;background:var(--white);margin-right:8px}
  .specialties{position:absolute;left:593px;top:469px;width:207px;height:250px;background:var(--blue);border-radius:10px;padding:8px 8px 8px 18px}
  .specialties h3{font-family:"Montserrat",sans-serif;font-weight:600;font-size:13.5px;line-height:19.5px;white-space:nowrap}
  .specialties p{margin-top:18px;font-size:15px;line-height:19.2px;white-space:nowrap}
  .feature{position:absolute;background:var(--card);color:var(--ink)}
  .feature h4{font-family:"Montserrat",sans-serif;font-weight:600;display:flex;align-items:center;white-space:nowrap}
  .feature p{color:var(--grey-text);font-size:16.5px;line-height:19px;white-space:nowrap}
  .f-gutter{left:337px;top:759px;width:233px;height:130px;padding:16px 8px}
  .f-gutter h4{font-size:20.5px;gap:14px}
  .f-gutter p{margin:12px 0 0 22px}
  .f-screen{left:584px;top:759px;width:220px;height:130px;padding:10px 8px}
  .f-screen h4{font-size:20.5px;gap:18px}
  .f-screen p{margin:16px 0 0 23px}
  .f-patio{left:43px;top:903px;width:280px;height:129px;padding:18px 26px}
  .f-patio h4{font-size:20.5px;gap:14px}
  .f-patio p{margin:8px 0 0 24px}
  .crew-note{position:absolute;left:337px;top:903px;width:467px;height:129px;background:var(--blue);padding:16px 18px;font-family:"Montserrat",sans-serif;font-weight:500;font-size:15px;line-height:17.6px;white-space:nowrap}
  .crew-note p+p{margin-top:15px}
  .cta{position:absolute;left:23px;top:1075px;width:798px;height:71px;background:var(--teal);display:flex;align-items:center;padding-left:11px;font-family:"Montserrat",sans-serif;font-weight:700;white-space:nowrap}
  .cta-label{font-size:26.5px;letter-spacing:.2px}
  .cta-phone{display:flex;align-items:center;gap:2px;margin-left:16px;font-size:46px;letter-spacing:-1px}
  .footnote{position:absolute;left:0;top:1164px;width:848px;text-align:center;font-family:"Montserrat",sans-serif;font-weight:600;font-size:14.2px;white-space:nowrap}
</style>
</head>
<body>
<main class="flyer">
  <div class="hero" role="img" aria-label="Photo of a house roofline with dormer window and new gutters under blue sky"></div>
  <div class="brand">HARTWELL<br>GUTTERS &amp; EXTERIORS</div>

  <div class="contact-phone">478.555.0142</div>
  <div class="contact-email">jhartwell@hartwellgutterspro.com</div>

  <div class="photo p1" role="img" aria-label="Photo of a gutter guard along a shingled roof edge"></div>
  <div class="photo framed-blue p2" role="img" aria-label="Photo of a bright patio cover interior with picnic table"></div>
  <div class="photo framed-blue p3" role="img" aria-label="Photo of a dark screened room attached to a brick house"></div>
  <div class="photo p4" role="img" aria-label="Photo of a sunroom interior with vinyl windows"></div>

  <h1 class="headline">Residential Rain Gutter &amp;<br>Screen room services</h1>
  <h2 class="services-title">SERVICES:</h2>
  <ul class="services-list">
    <li>Gutter Systems</li>
    <li>Gutter Cleaning</li>
    <li>Gutter Protection</li>
    <li>Patio Covers</li>
    <li>Screen Rooms</li>
    <li>Sunroom</li>
    <li>Vinyl Film Windows</li>
  </ul>

  <div class="specialties">
    <h3>Hartwell Gutters &amp;<br>Exteriors specializes<br>in the quality installa-<br>tion of:</h3>
    <p>Stillbrook Gutter Protec-<br>tion System<br>Seamless Aluminum<br>Gutters &amp; Downspouts<br>Gutter Cleaning<br>Patio Covers<br>Gutter Covers</p>
  </div>

  <section class="feature f-gutter">
    <h4><svg width="34" height="40" viewBox="0 0 34 40"><path d="M17 2 L32 16 L28 16 L28 38 L6 38 L6 16 L2 16 Z" fill="var(--ink)"/><rect x="12" y="22" width="10" height="14" fill="var(--card)"/></svg>Gutter Systems</h4>
    <p>Avoid Water Damage<br>with Proper Drainage</p>
  </section>
  <section class="feature f-screen">
    <h4><svg width="42" height="42" viewBox="0 0 36 38"><path d="M18 0 V8 M14 5 L18 9 L22 5" stroke="var(--ink)" stroke-width="2.5" fill="none"/><path d="M4 16 L18 12 L32 16 L32 34 L18 38 L4 34 Z" fill="var(--ink)"/><path d="M18 16 V38" stroke="var(--card)" stroke-width="2"/></svg>Screenroom</h4>
    <p>Enjoy Your Patio with a<br>Screen Room</p>
  </section>
  <section class="feature f-patio">
    <h4><svg width="44" height="44" viewBox="0 0 30 30"><circle cx="15" cy="15" r="12.5" fill="none" stroke="var(--ink)" stroke-width="2.5"/><text x="15" y="19.5" text-anchor="middle" font-family="Montserrat,sans-serif" font-weight="700" font-size="11" fill="var(--ink)">24</text></svg>Patio Covers</h4>
    <p>Built for entertaining and<br>shelter from the sun</p>
  </section>

  <div class="crew-note">
    <p>Meet our wonderful managerial staff &amp; great instal-<br>lation crews.</p>
    <p>We use high-quality products for all our installa-<br>tion including gutter, leaf protection, screen rooms<br>&amp; sunrooms</p>
  </div>

  <div class="cta">
    <span class="cta-label">CALL US FOR FREE ESTIMATE</span>
    <span class="cta-phone"><svg width="34" height="44" viewBox="0 0 30 40"><path d="M8 2 L14 10 L10 14 C10 20 14 26 18 30 L22 27 L28 34 L22 39 C10 36 2 22 3 6 Z" fill="var(--navy)"/></svg>478.555.0142</span>
  </div>
  <p class="footnote">At Hartwell Gutters and Exteriors we endeavor to answer all inquiries within 24 hours on business days.</p>
</main>
</body>
</html>
```